Business Card Design For Marketing Agnecy LVT

Need business card design for marketing agency.

Dorian Pell
President, CEO
1-555-304-2917
dorian@lumenvaletrewards.net
www.LumenValeTrewards.biz

Back Side:
Boost Sales Using Rewards, Incentives & Giveaways
Get A Free Sample Package

Target Market(s)

B2B

Industry/Entity Type

Marketing

Contact Information for Business Card

Dorian Pell
President, CEO
1-555-304-2917

Back Side:
Get A Free Sample Package

Please note that my current url is OLD DESIGN. I am working on new design and want the business card to match color themes at least on new site. Here is the demo link for new site so you can see the colors I use, etc.

http://pagekilnstudio.example/qx/dorian/lvt_final/index.html

Requirements
Must have
• Please note that my current url is OLD DESIGN. I am working on new design and want the business card to match color themes at least on new site. Here is the demo link for new site so you can see the colors I use, etc.

Nice to have

Should not have

```html
<!DOCTYPE html>
<html lang="en">
<head>
<meta charset="utf-8">
<title>LVT Business Card</title>
<link href="https://fonts.googleapis.com/css2?family=Montserrat:wght@400;500;700;800&display=swap" rel="stylesheet">
<style>
  :root {
    --brand-blue: #1176c0;
    --ink-grey: #5a5b5e;
    --paper: #ffffff;
    --backdrop: #e9e7e4;
  }
  html, body {
    margin: 0;
    padding: 0;
    width: 1200px;
    height: 909px;
    overflow: hidden;
    background: var(--backdrop);
    font-family: "Montserrat", Arial, sans-serif;
  }
  .canvas {
    position: relative;
    width: 1200px;
    height: 909px;
  }
  .card {
    position: absolute;
    width: 640px;
    height: 366px;
    border-radius: 22px;
    overflow: hidden;
    box-shadow: 0 6px 18px rgba(0,0,0,0.18);
  }

  /* Back side */
  .card-back {
    left: 70px;
    top: 80px;
    background: var(--brand-blue);
  }
  .card-back .brand-name {
    position: absolute;
    left: 0;
    right: 0;
    top: 78px;
    text-align: center;
    color: var(--paper);
    font-weight: 800;
    font-size: 112px;
    letter-spacing: 4px;
    line-height: 1;
  }
  .card-back .site-url {
    position: absolute;
    left: 0;
    right: 0;
    top: 262px;
    text-align: center;
    color: var(--paper);
    font-size: 14px;
    font-weight: 500;
    letter-spacing: 0.3px;
  }
  .card-back .tagline-band {
    position: absolute;
    left: 0;
    right: 0;
    top: 298px;
    height: 34px;
    background: var(--paper);
    color: var(--ink-grey);
    font-size: 13.5px;
    font-weight: 500;
    display: flex;
    align-items: center;
    justify-content: center;
    white-space: nowrap;
  }

  /* Front side */
  .card-front {
    left: 490px;
    top: 460px;
    background: var(--paper);
  }
  .card-front .swoosh {
    position: absolute;
    inset: 0;
  }
  .card-front .brand-block {
    position: absolute;
    left: 40px;
    top: 118px;
    width: 300px;
    text-align: center;
  }
  .card-front .brand-name {
    display: block;
    color: var(--brand-blue);
    font-weight: 800;
    font-size: 92px;
    line-height: 1;
    letter-spacing: 3px;
  }
  .card-front .contact {
    position: absolute;
    right: 34px;
    top: 128px;
    text-align: right;
    color: var(--paper);
  }
  .contact .person-name {
    font-weight: 800;
    font-size: 22px;
    letter-spacing: 0.3px;
    margin: 0;
  }
  .contact .person-role {
    font-size: 15px;
    margin: 2px 0 0;
  }
  .contact .divider {
    width: 46px;
    height: 1px;
    background: var(--paper);
    margin: 10px 0 14px auto;
  }
  .contact .line {
    display: flex;
    justify-content: flex-end;
    align-items: center;
    gap: 8px;
    font-size: 14px;
    margin: 0 0 6px;
  }
  .contact .line svg {
    width: 12px;
    height: 12px;
    flex: none;
  }
</style>
</head>
<body>
<div class="canvas">

  <section class="card card-back" aria-label="Card back side">
    <div class="brand-name">LVT</div>
    <div class="site-url">www.LumenValeTrewards.biz</div>
    <div class="tagline-band">Boost Sales Using Rewards | Incentives &amp; Giveaways | Get A Free Sample Package</div>
  </section>

  <section class="card card-front" aria-label="Card front side">
    <svg class="swoosh" viewBox="0 0 640 366" width="640" height="366" aria-hidden="true">
      <path d="M150 366 Q420 250 458 0" fill="none" stroke="#5a5b5e" stroke-width="5"/>
      <path d="M170 366 Q432 252 470 0 L640 0 L640 366 Z" fill="#1176c0"/>
    </svg>

    <div class="brand-block">
      <span class="brand-name">LVT</span>
    </div>

    <div class="contact">
      <p class="person-name">DORIAN PELL</p>
      <p class="person-role">President, CEO</p>
      <div class="divider"></div>
      <p class="line">1-555-304-2917
        <svg viewBox="0 0 24 24"><path fill="#ffffff" d="M6.6 10.8a15.1 15.1 0 0 0 6.6 6.6l2.2-2.2a1 1 0 0 1 1-.25 11.4 11.4 0 0 0 3.6.57 1 1 0 0 1 1 1V20a1 1 0 0 1-1 1A17 17 0 0 1 3 4a1 1 0 0 1 1-1h3.5a1 1 0 0 1 1 1c0 1.25.2 2.45.57 3.57a1 1 0 0 1-.25 1z"/></svg>
      </p>
      <p class="line">dorian@lumenvaletrewards.net
        <svg viewBox="0 0 24 24"><rect x="2" y="5" width="20" height="14" fill="#ffffff"/><path d="M2 5l10 8 10-8" fill="none" stroke="#1176c0" stroke-width="2"/></svg>
      </p>
      <p class="line">www.LumenValeTrewards.biz
        <svg viewBox="0 0 24 24"><circle cx="12" cy="12" r="10" fill="#ffffff"/></svg>
      </p>
    </div>
  </section>

</div>
</body>
</html>
```